Web Design Project

We need a website for a new public relations firm offering PR, advertising, media buying, design and social media. Target clients are professional service firms such as lawyers or CPAs. Looks should be clean and look expensive.

Target Market(s)

Professional service firms. Think business to business companies like consultancy firms.

Industry/Entity Type

Professional Service

Colors

Designer to choose colors to be used in the design.

Requirements
Must have
• Site pages for the purpose of design will include Home, Services, Experience, Bios and Contact Us

```html
<!DOCTYPE html>
<html lang="en">
<head>
<meta charset="utf-8">
<title>Halvern – Public Relations</title>
<link href="https://fonts.googleapis.com/css2?family=Lato:wght@400;700;900&display=swap" rel="stylesheet">
<style>
:root{
  --dark:#3a3a3a;
  --light:#f5f5f5;
  --white:#ffffff;
  --green:#5cc49a;
  --muted:#9a9a9a;
  --heading:#555555;
  --rule:#dddddd;
  --hero-top:#d2d9db;
  --hero-bottom:#c4c6c3;
}
*{margin:0;padding:0;box-sizing:border-box}
html,body{width:1200px;height:2268px;overflow:hidden}
body{font-family:'Lato',Arial,sans-serif;background:var(--white);color:var(--heading);position:relative}
.site-header{position:absolute;left:0;top:0;width:1200px;height:62px;background:var(--dark)}
.brand{position:absolute;left:95px;top:18px;color:var(--white);font-size:20px;font-weight:400;letter-spacing:1px}
.header-divider{position:absolute;left:208px;top:14px;width:1px;height:34px;background:#777}
.main-nav a{position:absolute;top:21px;color:var(--white);font-size:14px;font-weight:700;text-decoration:none}
.social{position:absolute;top:17px;width:26px;height:26px;border:2px solid var(--white)}
.hero{position:absolute;left:0;top:62px;width:1200px;height:463px;background:linear-gradient(180deg,var(--hero-top),var(--hero-bottom))}
.hero-arrow{position:absolute;top:235px;width:60px;height:54px;background:rgba(255,255,255,.6)}
.hero-arrow.prev{left:0}.hero-arrow.next{right:0}
.services{position:absolute;left:0;top:525px;width:1200px;height:439px;background:var(--light)}
.service{position:absolute;width:300px}
.service-icon{position:absolute;left:0;top:-2px}
.service h3{position:absolute;left:82px;top:0;font-size:17.5px;font-weight:700;color:var(--heading);white-space:nowrap}
.service p{position:absolute;left:82px;top:32px;width:200px;font-size:11.5px;line-height:16px;color:var(--muted)}
.service .more{position:absolute;left:82px;top:86px;font-size:11px;color:#666;white-space:nowrap}
.vline{position:absolute;left:600px;width:1px;background:var(--rule)}
.testimonials{position:absolute;left:0;top:964px;width:1200px;height:457px;text-align:center}
.testimonials h2{position:absolute;left:0;top:108px;width:1200px;font-size:21px;font-weight:400;letter-spacing:1.5px;color:#444}
.quote{position:absolute;left:185px;top:184px;width:830px;font-size:15.5px;line-height:25.5px;color:var(--muted);letter-spacing:.3px}
.author{position:absolute;left:0;top:287px;width:1200px;font-size:12px;font-weight:700;color:#444}
.dots{position:absolute;left:576px;top:333px}
.networking{position:absolute;left:0;top:1421px;width:1200px;height:323px}
.networking-photo{position:absolute;left:0;top:0;width:600px;height:323px;background:linear-gradient(135deg,#dcdad6 0%,#ecebe8 50%,#cfcbc5 100%)}
.networking-panel{position:absolute;left:600px;top:0;width:600px;height:323px;background:var(--dark);color:var(--white)}
.networking-panel h2{position:absolute;left:31px;top:62px;font-size:24px;font-weight:700;letter-spacing:1.5px}
.networking-panel p{position:absolute;left:31px;top:154px;width:525px;font-size:12.5px;font-weight:700;line-height:27px}
.networking-panel .more{position:absolute;left:31px;top:246px;font-size:12.5px;font-weight:700}
.cta{position:absolute;left:0;top:1744px;width:1200px;height:303px;text-align:center}
.cta h2{position:absolute;left:0;top:74px;width:1200px;font-size:26px;font-weight:700;color:#666;letter-spacing:2px}
.cta-button{position:absolute;left:495px;top:178px;width:210px;height:44px;background:var(--dark);color:var(--white);font-size:15px;font-weight:700;line-height:44px;text-align:center}
.site-footer{position:absolute;left:0;top:2047px;width:1200px;height:221px;background:var(--light);border-top:1px solid #e5e5e5;text-align:center}
.footer-brand{position:absolute;left:0;top:60px;width:1200px;font-size:20px;color:#555;letter-spacing:1px}
.copyright{position:absolute;left:0;top:130px;width:1200px;font-size:10.5px;color:#222}
</style>
</head>
<body>
<header class="site-header">
  <div class="brand">Halvern</div>
  <div class="header-divider"></div>
  <nav class="main-nav">
    <a style="left:240px">Home</a>
    <a style="left:319px">Services</a>
    <a style="left:414px">Experience</a>
    <a style="left:525px">Bios</a>
    <a style="left:593px">Contact Us</a>
  </nav>
  <span class="social" style="left:979px"></span>
  <span class="social" style="left:1016px"></span>
  <span class="social" style="left:1052px"></span>
</header>

<section class="hero" role="img" aria-label="Photo of a pelican perched on a wooden post beside a pier over the sea">
  <div class="hero-arrow prev"><svg width="60" height="54"><path d="M33 19l-8 8 8 8" fill="none" stroke="#333" stroke-width="2"/></svg></div>
  <div class="hero-arrow next"><svg width="60" height="54"><path d="M27 19l8 8-8 8" fill="none" stroke="#333" stroke-width="2"/></svg></div>
</section>

<section class="services">
  <div class="service" style="left:120px;top:82px">
    <svg class="service-icon" width="52" height="52"><circle cx="26" cy="26" r="26" fill="#5cc49a"/><rect x="18" y="17" width="16" height="7" rx="1" fill="none" stroke="#fff" stroke-width="2"/><path d="M34 20h2v7h-9v4" fill="none" stroke="#fff" stroke-width="2"/><rect x="25" y="31" width="4" height="8" fill="#fff"/></svg>
    <h3>Design and Social Media.</h3>
    <p>Coccaecat cupidatat aliqu proident sunt in culpa qui officia deserunt mollit anim.</p>
    <span class="more">more details &rarr;</span>
  </div>
  <div class="service" style="left:462px;top:82px">
    <svg class="service-icon" width="52" height="52"><circle cx="26" cy="26" r="26" fill="#5cc49a"/><rect x="15" y="17" width="22" height="15" rx="2" fill="none" stroke="#fff" stroke-width="2"/><path d="M22 37h8M26 32v5" stroke="#fff" stroke-width="2"/></svg>
    <h3>Advertising.</h3>
    <p>Coccaecat cupidatat aliqu proident sunt in culpa qui officia deserunt mollit anim.</p>
    <span class="more">more details &rarr;</span>
  </div>
  <div class="service" style="left:804px;top:82px">
    <svg class="service-icon" width="52" height="52"><circle cx="26" cy="26" r="26" fill="#5cc49a"/><rect x="20" y="14" width="13" height="23" rx="2" fill="none" stroke="#fff" stroke-width="2"/><path d="M24 20h5M24 24h5M24 28h5" stroke="#fff" stroke-width="1.5"/></svg>
    <h3>Public Relations.</h3>
    <p>Coccaecat cupidatat aliqu proident sunt in culpa qui officia deserunt mollit anim.</p>
    <span class="more">more details &rarr;</span>
  </div>
  <div class="service" style="left:469px;top:273px">
    <svg class="service-icon" width="52" height="52"><circle cx="26" cy="26" r="26" fill="#5cc49a"/><rect x="14" y="18" width="24" height="16" rx="2" fill="none" stroke="#fff" stroke-width="2"/><path d="M14 23h24M18 29h6M30 29h4" stroke="#fff" stroke-width="2"/></svg>
    <h3>Media Buying</h3>
    <p>Coccaecat cupidatat aliqu proident sunt in culpa qui officia deserunt mollit anim.</p>
    <span class="more">more details &rarr;</span>
  </div>
</section>

<div class="vline" style="top:964px;height:80px"></div>
<section class="testimonials">
  <h2>TESTIMONIALS</h2>
  <p class="quote">Sed do eiusmod tempor incididunt ut labore et dolore magna aliqua. Ut enim ad minim veniam quis nostrud exercitation ullamco laboris nisi ut aliquip ex ea commodo consequat. Duis aute irure dolor in reprehenderit in voluptate velit esse cillum dolore eu pariatur.</p>
  <div class="author">John Doe - JD/PR</div>
  <svg class="dots" width="48" height="12"><circle cx="6" cy="6" r="5" fill="#c4c4c4"/><circle cx="24" cy="6" r="5" fill="#e2e2e2"/><circle cx="42" cy="6" r="5" fill="#e2e2e2"/></svg>
</section>
<div class="vline" style="top:1340px;height:81px"></div>

<section class="networking">
  <div class="networking-photo" role="img" aria-label="Photo of hands holding a smartphone over papers on a desk"></div>
  <div class="networking-panel">
    <h2>NETWORKING IS KEY.</h2>
    <p>Magna aliqua ut enim ad minim veniam, quis nostrud exercitation ullamco laboris nisi ut aliquip ex ea commodo consequat duis aute irure dolor in reprehenderit in voluptate velit esse cillum.</p>
    <span class="more">More Details &rarr;</span>
  </div>
</section>

<section class="cta">
  <h2>TAKE ACTION &amp; AND LET’S GET STARTED !</h2>
  <div class="cta-button">SIGN UP NOW!</div>
</section>
<div class="vline" style="top:1966px;height:81px"></div>

<footer class="site-footer">
  <div class="footer-brand">Halvern</div>
  <div class="copyright">Copyright © Halvern - All rights reserved.</div>
</footer>
</body>
</html>
```